The Larkspur Whiskey & Coffee - Bar Menu

The Larkspur is a speakeasy style coffee and whiskey bar. Upscale with design elements tying in both prohibition era elegance and modern touches.

Black and Gold are our colors. (see logo)

We would need a 8 page menu- front and back. 4.24 in x 11 in for each page. The pages would be:

Intro page
Food/Dessert
Cocktails x 2 pages
Wine- Glass Pour
Wine- Bottle only
Beer
Non-Alcoholic Beverages

Attached is the menu cocktails and food/non alcoholic.

We need an editable format as this menu would be constantly changing.

UPDATE: The owner would potentially like to see the use of the original floor plans incorporated into the menu design. I have uploaded those to this brief.

UPDATE: I have added some photos that show the style the owner would like the writing to be displayed.

Requirements
Should not have
• No pictures of wine or beer or other images. Clipart could be fine, but we want to showcase class and an upscale vibe.

```html
<!DOCTYPE html>
<html lang="en">
<head>
<meta charset="utf-8">
<title>The Larkspur Whiskey &amp; Coffee – Bar Menu</title>
<link href="https://fonts.googleapis.com/css2?family=Bebas+Neue&family=Poppins:wght@400;500;600&display=swap" rel="stylesheet">
<style>
:root{
  --backdrop:#e9cf96;
  --gold:#d7a93f;
  --gold-deep:#a8782a;
  --gold-pattern:#d9b25b;
  --ink:#0d0c0b;
  --paper:#ffffff;
  --plan:#e6e6e6;
}
*{margin:0;padding:0;box-sizing:border-box}
html,body{width:1200px;height:781px;overflow:hidden}
body{background:var(--backdrop);position:relative;font-family:"Poppins",sans-serif;color:var(--ink)}
.page{position:absolute;width:222px;height:577px;background:var(--paper);box-shadow:0 4px 14px rgba(120,90,30,.18);overflow:hidden}
.floor-plan{position:absolute;left:0;right:0;bottom:0;background:linear-gradient(to bottom,rgba(230,230,230,0),var(--plan) 45%,#dcdcdc)}
/* cover */
.cover-pattern{position:absolute;left:0;top:0;width:222px;height:305px;background:var(--gold-pattern)}
.ribbon{position:absolute;left:37px;top:0;width:153px;height:392px}
.ribbon svg{position:absolute;inset:0}
.cover-name{position:absolute;left:0;right:0;text-align:center;font-family:"Bebas Neue",sans-serif;color:var(--gold);line-height:1}
.cover-name .title{display:block;font-size:23px;letter-spacing:1px}
.cover-name .sub{display:block;font-size:9px;letter-spacing:1px;margin-top:1px}
.notice{position:absolute;left:10px;right:10px;text-align:center;color:#fff;font-size:5.7px;line-height:1.25}
.notice b{font-weight:600}
.divider{position:absolute;left:32px;width:89px;height:6px}
/* tabs */
.tab{position:absolute;left:78px;top:0;width:66px;height:67px}
.tab svg{position:absolute;inset:0}
.tab-name{position:absolute;left:0;right:0;top:38px;text-align:center;font-family:"Bebas Neue",sans-serif;color:var(--gold);line-height:1}
.tab-name .title{display:block;font-size:9.5px;letter-spacing:.5px}
.tab-name .sub{display:block;font-size:3.6px;letter-spacing:.3px}
/* frames */
.frame{position:absolute}
.frame svg{position:absolute;inset:0}
.section-title{position:absolute;left:0;right:0;text-align:center;font-family:"Bebas Neue",sans-serif;color:var(--gold);font-size:24px;line-height:1;letter-spacing:1px}
.section-title::before,.section-title::after{content:"◆";font-size:7px;vertical-align:middle;margin:0 4px;position:relative;top:-2px}
.spirit{position:absolute;left:0;right:0;text-align:center;color:var(--gold);font-size:7px;font-weight:500;line-height:1}
.spirit::before,.spirit::after{content:"◆";font-size:4px;vertical-align:middle;margin:0 2px}
.item{position:absolute;border-bottom:.6px solid var(--gold)}
.item .name{display:block;color:var(--gold);font-size:5px;line-height:1.2}
.item .desc{display:block;font-size:4.3px;line-height:1.2;margin-top:3px}
.dish{position:absolute;left:11px;width:156px}
.dish .row{display:flex;align-items:center;color:var(--gold);font-size:4.8px;line-height:1.2}
.dish .row::after{content:"";order:1;flex:1;height:.5px;background:var(--gold);margin:0 3px}
.dish .price{order:2}
.dish .desc{font-size:4.3px;line-height:1.25;margin-top:.5px}
.dessert-name{position:absolute;color:var(--gold);font-size:10px;font-weight:500;line-height:1}
.dessert-desc{position:absolute;font-size:4.4px;line-height:1.3}
.sketch{position:absolute;background:radial-gradient(ellipse at center,#f1dfb3,#fff 75%)}
</style>
</head>
<body>

<!-- Cover page -->
<section class="page cover" style="left:91px;top:50px">
  <div class="cover-pattern" role="img" aria-label="Gold art deco lattice pattern"></div>
  <div class="floor-plan" style="top:440px" role="img" aria-label="Architectural elevation drawing of the historic building"></div>
  <div class="ribbon">
    <svg viewBox="0 0 153 392" width="153" height="392">
      <polygon points="0,0 153,0 153,392 76.5,374 0,392" fill="#0d0c0b"/>
      <polyline points="9,0 9,377 76.5,359 144,377 144,0" fill="none" stroke="#d7a93f" stroke-width=".8"/>
    </svg>
    <div class="cover-name" style="top:107px">
      <span class="title">The Larkspur</span>
      <span class="sub">Whiskey &amp; Coffee</span>
    </div>
  </div>
  <p class="notice" style="top:197px">The Larkspur Whiskey &amp; Coffee<br>Reserves the right to change<br>menus selections, and/or the<br>prices that accompany those</p>
  <svg class="divider" style="top:230px;left:69px" viewBox="0 0 89 6"><line x1="0" y1="3" x2="89" y2="3" stroke="#d7a93f" stroke-width=".6"/><circle cx="1.5" cy="3" r="1.3" fill="#d7a93f"/><circle cx="87.5" cy="3" r="1.3" fill="#d7a93f"/><polygon points="44.5,0 47.5,3 44.5,6 41.5,3" fill="#0d0c0b" stroke="#d7a93f" stroke-width=".6"/></svg>
  <p class="notice" style="top:243px">Only one promotion/spe-<br>cial/discount/kickback<br>may be used at one time,<br>per table or check</p>
  <svg class="divider" style="top:280px;left:69px" viewBox="0 0 89 6"><line x1="0" y1="3" x2="89" y2="3" stroke="#d7a93f" stroke-width=".6"/><circle cx="1.5" cy="3" r="1.3" fill="#d7a93f"/><circle cx="87.5" cy="3" r="1.3" fill="#d7a93f"/><polygon points="44.5,0 47.5,3 44.5,6 41.5,3" fill="#d7a93f"/></svg>
  <p class="notice" style="top:294px"><b>20%</b> service charged<br>added onto bills of parties</p>
</section>

<!-- Food & dessert page -->
<section class="page" style="left:361px;top:103px">
  <div class="floor-plan" style="top:455px" role="img" aria-label="Faded architectural elevation of the building"></div>
  <div class="tab">
    <svg viewBox="0 0 66 67"><polygon points="0,0 66,0 66,66 33,63 0,67" fill="#0d0c0b"/></svg>
    <div class="tab-name"><span class="title">The Larkspur</span><span class="sub">Whiskey &amp; Coffee</span></div>
  </div>

  <div class="frame" style="left:20px;top:96px;width:178px;height:201px">
    <svg viewBox="0 0 178 201"><path d="M10,.5H168A10,10 0 0 0 177.5,10V191A10,10 0 0 0 168,200.5H10A10,10 0 0 0 .5,191V10A10,10 0 0 0 10,.5Z" fill="#fff" stroke="#a8782a" stroke-width=".8"/></svg>
    <h2 class="section-title" style="top:14px">Food</h2>
    <div class="dish" style="top:57px"><div class="row">Bone marrow<span class="price">$20</span></div><div class="desc">Bone marrow roasted with sea salt and served with warm tortillas</div></div>
    <div class="dish" style="top:79px"><div class="row">Charcuterie board<span class="price">$25</span></div><div class="desc">Assorted artisan meats and cheeses, nuts, and fruits</div></div>
    <div class="dish" style="top:98px"><div class="row">Hummus, Veggie, &amp; Pita<span class="price">$16</span></div><div class="desc">Assorted vegetables with warm pita and roasted garlic hummus</div></div>
    <div class="dish" style="top:116px"><div class="row">Lamb Chops<span class="price">$18</span></div><div class="desc">Lamb chops broiled with rosemary</div></div>
    <div class="dish" style="top:136px"><div class="row">Tuna Tower<span class="price">$17</span></div><div class="desc">Fresh tuna served with white rice, avocado and spice</div></div>
    <div class="dish" style="top:156px"><div class="row">Lettuce Wrap- Walnut Shrimp<span class="price">$13</span></div><div class="desc">Honey walnut aioli coated shrimp and lettuce cups with a<br>candied walnut</div></div>
  </div>

  <div class="frame" style="left:20px;top:329px;width:178px;height:201px">
    <svg viewBox="0 0 178 201"><path d="M10,.5H168A10,10 0 0 0 177.5,10V191A10,10 0 0 0 168,200.5H10A10,10 0 0 0 .5,191V10A10,10 0 0 0 10,.5Z" fill="#fff" stroke="#a8782a" stroke-width=".8"/></svg>
    <h2 class="section-title" style="top:16px">Dessert</h2>
    <div class="dessert-name" style="left:19px;top:77px">Tart</div>
    <p class="dessert-desc" style="left:19px;top:91px">Your choice of apple or<br>berry with vanilla ice cream</p>
    <div class="sketch" style="left:104px;top:65px;width:55px;height:43px" role="img" aria-label="Gold line sketch of a dessert on a plate"></div>
    <div class="sketch" style="left:19px;top:121px;width:47px;height:39px" role="img" aria-label="Gold line sketch of a cake slice"></div>
    <div class="dessert-name" style="left:93px;top:135px">Cheesecake</div>
    <p class="dessert-desc" style="left:93px;top:148px">Chocolate or strawberry drizzle</p>
  </div>
</section>

<!-- Cocktails page one -->
<section class="page" style="left:619px;top:50px">
  <div class="floor-plan" style="top:460px" role="img" aria-label="Faded architectural elevation of the building"></div>
  <div class="tab">
    <svg viewBox="0 0 66 67"><polygon points="0,0 66,0 66,67 33,64 0,66" fill="#0d0c0b"/></svg>
    <div class="tab-name"><span class="title">The Larkspur</span><span class="sub">Whiskey &amp; Coffee</span></div>
  </div>
  <div class="frame" style="left:20px;top:95px;width:179px;height:435px">
    <svg viewBox="0 0 179 435"><path d="M10,.5H169A10,10 0 0 0 178.5,10V425A10,10 0 0 0 169,434.5H10A10,10 0 0 0 .5,425V10A10,10 0 0 0 10,.5Z" fill="#fff" stroke="#a8782a" stroke-width=".8"/></svg>
    <h2 class="section-title" style="top:14px">Cocktails</h2>
    <div class="spirit" style="top:50px">VODKA</div>
    <div class="item" style="left:15px;width:146px;top:64px;height:23px"><span class="name">The Affair</span><span class="desc">Vodka (strawberry/orange infusion), Lemon Oleo Saccahrum,<br>PeaFlower Gin Float(Blue) (N&amp;N)</span></div>
    <div class="item" style="left:15px;width:146px;top:91px;height:23px"><span class="name">Bootleggers Gold</span><span class="desc">Vodka, Yellow Herbal Liqueur, Pineapple, Lime Juice, Simple Syrup,<br>Lemon Zes</span></div>
    <div class="spirit" style="top:128px">TEQUILA</div>
    <div class="item" style="left:15px;width:146px;top:137px;height:22px;border:0"><span class="name">The Mayan</span><span class="desc">Casa Alta Blanco, Raicilla (non-peaty Mezcal), Green Herbal Liqueur,<br>Pistachio Liqueur, Olive, Lime</span></div>
    <div class="item" style="left:15px;width:146px;top:166px;height:22px;border:0"><span class="name">Toreador*</span><span class="desc">Blanco, Mezcal, Apricot Cordial, Lime Juice, GrapeFruit oil(oleo),<br>Mezcal Mist</span></div>
    <div class="spirit" style="top:196px">RUM</div>
    <div class="item" style="left:15px;width:146px;top:211px;height:26px"><span class="name">Smugglers Cove**</span><span class="desc">Rum (Cuban), Pomegranite Liqueur, Lemon Juice, Macadamia<br>Orgeat, Cocoa Bitters (Eggwhite)</span></div>
    <div class="item" style="left:15px;width:146px;top:242px;height:22px"><span class="name">Mary Pennington*</span><span class="desc">Rum (Blanco Cuban), Pineapple, Maraschino Liqueur, Grenadine</span></div>
    <div class="item" style="left:15px;width:146px;top:269px;height:26px"><span class="name">Roy Rum Runner (Local)</span><span class="desc">Rum (Blanco), Rhum Agricole (non-peat Mezcal) Lime Juice,<br>Simple Syrup w/in season fruit</span></div>
    <div class="spirit" style="top:305px">GIN</div>
    <div class="item" style="left:15px;width:146px;top:317px;height:25px"><span class="name">Clover Club*</span><span class="desc">Azure Gin, Rasperry Liquor, Lemon Juice, Raspberries, Vanilla,<br>Prosecco, Milk (Clarified)</span></div>
    <div class="item" style="left:15px;width:146px;top:346px;height:19px"><span class="name">Clover Club#2**</span><span class="desc">Gin, Dry Vermouth, Raspberry, Lemon Juice, EggWhite</span></div>
    <div class="item" style="left:15px;width:146px;top:370px;height:26px"><span class="name">Limonata</span><span class="desc">Gin (Lemon infused), Limoncello, Lemon Curd, Lemon Juice,<br>Sparkling Limonata</span></div>
    <div class="item" style="left:15px;width:146px;top:401px;height:18px"><span class="name">Colony Cocktail</span><span class="desc">Gin, Pink Grapefruit, Maraschino Liqueur, Grapefruit twist</span></div>
  </div>
</section>

<!-- Cocktails page two -->
<section class="page" style="left:877px;top:103px">
  <div class="floor-plan" style="top:455px" role="img" aria-label="Faded architectural elevation of the building"></div>
  <div class="tab">
    <svg viewBox="0 0 66 67"><polygon points="0,0 66,0 66,66 33,63 0,67" fill="#0d0c0b"/></svg>
    <div class="tab-name"><span class="title">The Larkspur</span><span class="sub">Whiskey &amp; Coffee</span></div>
  </div>
  <div class="frame" style="left:21px;top:96px;width:179px;height:434px">
    <svg viewBox="0 0 179 434"><path d="M10,.5H169A10,10 0 0 0 178.5,10V424A10,10 0 0 0 169,433.5H10A10,10 0 0 0 .5,424V10A10,10 0 0 0 10,.5Z" fill="#fff" stroke="#a8782a" stroke-width=".8"/></svg>
    <h2 class="section-title" style="top:14px">Cocktails</h2>
    <div class="spirit" style="top:50px">WHISKEY</div>
    <div class="item" style="left:13px;width:146px;top:64px;height:22px"><span class="name">The Dark Walnut</span><span class="desc">Irish Whiskey, Walnut Liqueur, Agave Nectar, Expresso</span></div>
    <div class="item" style="left:13px;width:146px;top:94px;height:27px"><span class="name">Penicillin*</span><span class="desc">Blended Scotch, Islay Peat, Lemon Juice, Ginger, Honey Syrup (R)(Candied<br>Ginger Garnish)</span></div>
    <div class="item" style="left:13px;width:146px;top:128px;height:21px"><span class="name">Albert Hollis (Local Bootlegger)</span><span class="desc">Kentucky Bourbon, Honey Liqueur, Lemon Juice, Habanero Bitters</span></div>
    <div class="item" style="left:13px;width:146px;top:159px;height:22px"><span class="name">Rockwell** (NY Sour)</span><span class="desc">Bourbon, Demerara Simple Syrup, Lemon Juice, Redwine Float</span></div>
    <div class="item" style="left:13px;width:146px;top:189px;height:27px"><span class="name">Decadence</span><span class="desc">Blended Scotch/Whiskey, Sweet Sherry, Dry Sherry, Chocolate Bitters,<br>Orange, Raspberry</span></div>
    <div class="item" style="left:13px;width:146px;top:224px;height:22px"><span class="name">Gold Rush**</span><span class="desc">Bourbon, Honey Syrup, Amaro, Lemon Juice (Eggwhite)</span></div>
    <div class="spirit" style="top:281px">CORDIALS</div>
    <div class="item" style="left:13px;width:146px;top:297px;height:22px"><span class="name">The Wax Poet</span><span class="desc">Cognac, Beeswax, Toasted Almond Liqueur, Marigold Liqueur, Lime</span></div>
    <div class="item" style="left:13px;width:146px;top:329px;height:26px"><span class="name">The Bohemian</span><span class="desc">Cognac, Brown Butter, Dark Rum, Orange Liqueur, Pear Liqueur,<br>Bitters</span></div>
  </div>
</section>

</body>
</html>
```